Brightvale Marketing Banner for emails to customers

Hi Marketing Team The information is to be a nice banner say half page on Marketing our Services to prospective customers, this is embedded into an email so something nice with the content that I will provide. Based on a nice background to highlight our service portfolio aligned to our website
www.brightvale.com.au

```html
<!DOCTYPE html>
<html lang="en">
<head>
<meta charset="utf-8">
<title>Brightvale Marketing Banner</title>
<link href="https://fonts.googleapis.com/css2?family=Roboto+Slab:wght@300;400;700&display=swap" rel="stylesheet">
<style>
  :root {
    --navy: #2b3f6c;
    --navy-deep: #1d2b4d;
    --orange: #cd5227;
    --white: #ffffff;
    --card-grey: #f1f1f1;
    --body-text: #4a4a4a;
    --bullet: #8088b4;
  }
  * { margin: 0; padding: 0; box-sizing: border-box; }
  html, body { width: 1200px; height: 1200px; overflow: hidden; }
  body { font-family: "Roboto Slab", Georgia, serif; background: var(--white); }
  .banner { position: relative; width: 1200px; height: 1200px; overflow: hidden; background: var(--navy); }
  .kitchen-photo {
    position: absolute; left: 0; top: 0; width: 1200px; height: 760px;
    background: linear-gradient(160deg, #22345c 0%, #34497a 35%, #1f2f55 70%, var(--navy) 100%);
  }
  .logo-tab {
    position: absolute; left: 168px; top: 52px; width: 626px; height: 160px;
    background: var(--white); border-radius: 50px 50px 0 0;
  }
  .brand { position: absolute; left: 52px; top: 36px; display: flex; align-items: center; gap: 20px; }
  .brand-dot { width: 64px; height: 64px; border-radius: 50%; background: var(--navy); }
  .brand-name { font-size: 72px; font-weight: 400; color: var(--orange); line-height: 1; }
  .brand-url { position: absolute; left: 166px; top: 112px; font-size: 28px; font-weight: 400; color: var(--orange); }
  .intro {
    position: absolute; left: 168px; top: 203px; width: 1032px; height: 274px;
    background: var(--orange); border-radius: 0 0 0 50px; color: var(--white);
    padding: 30px 40px 0 48px;
  }
  .intro h1 { font-size: 36px; font-weight: 700; letter-spacing: -0.5px; margin-bottom: 16px; }
  .intro p { font-size: 25px; font-weight: 300; line-height: 1.25; margin-bottom: 22px; }
  .intro strong { font-weight: 700; }
  .cards { position: absolute; left: 61px; top: 528px; width: 1079px; height: 488px; display: flex; box-shadow: 0 6px 18px rgba(0,0,0,.35); }
  .card { flex: 1; text-align: center; padding-top: 20px; }
  .card-portfolio { background: var(--white); }
  .card-upgrades { background: var(--card-grey); box-shadow: inset 14px 0 16px -10px rgba(0,0,0,.3); }
  .card-icon { width: 110px; height: 120px; display: block; margin: 0 auto; }
  .card h2 { font-size: 40px; font-weight: 700; line-height: 1.05; margin-top: 18px; }
  .card h2 .accent { color: var(--orange); display: block; }
  .card h2 .dark { color: var(--navy); display: block; }
  .service-list { list-style: none; text-align: left; margin: 18px 0 0 92px; font-size: 23px; font-weight: 300; color: var(--body-text); line-height: 1.24; }
  .service-list li { position: relative; padding-left: 38px; }
  .service-list li.bulleted::before { content: ""; position: absolute; left: 6px; top: 9px; width: 12px; height: 12px; border-radius: 50%; background: var(--bullet); }
  .upgrade-text { text-align: justify; margin: 18px 80px 0 86px; font-size: 23px; font-weight: 300; color: var(--body-text); line-height: 1.27; }
  .upgrade-text + .upgrade-text { margin-top: 26px; }
  .service-panel { position: absolute; left: 0; top: 1056px; width: 1200px; height: 144px; }
  .contact { position: absolute; right: 68px; top: 1068px; text-align: right; color: var(--navy); }
  .contact h3 { font-size: 36px; font-weight: 700; line-height: 1.1; }
  .contact p { font-size: 22px; font-weight: 400; line-height: 1.3; }
</style>
</head>
<body>
<div class="banner">
  <div class="kitchen-photo" role="img" aria-label="Commercial kitchen interior with stainless steel benches and exhaust hoods, tinted dark blue"></div>

  <div class="logo-tab">
    <div class="brand">
      <span class="brand-dot"></span>
      <span class="brand-name">Brightvale</span>
    </div>
    <div class="brand-url">www.brightvale.com.au</div>
  </div>

  <section class="intro">
    <h1>Hope you are keeping well during this time.</h1>
    <p><strong>Brightvale</strong> has been in business for 15 years and built a strong and steady market reputation.</p>
    <p>Please find attached our Brightvale Marketing Brochure detailing our dedicated portfolio offerings for your perusal.</p>
  </section>

  <div class="cards">
    <div class="card card-portfolio">
      <svg class="card-icon" viewBox="0 0 110 120" fill="none" stroke="#cd5227" stroke-width="5" stroke-linejoin="round" stroke-linecap="round">
        <circle cx="55" cy="30" r="11"/>
        <path d="M50 42v8h10v-8"/>
        <path d="M55 6v4M36 14l3 3M74 14l-3 3M30 30h4M76 30h4"/>
        <path d="M10 66l45-12 45 12-45 12z"/>
        <path d="M18 70v34l37 12 37-12V70"/>
        <path d="M55 78v38"/>
        <path d="M10 66l-6 14 40 10 11-12M100 66l6 14-40 10-11-12"/>
      </svg>
      <h2><span class="accent">Portfolio</span><span class="dark">of Services:</span></h2>
      <ul class="service-list">
        <li class="bulleted">Equipment Sundae Machine Cleaning Service.</li>
        <li class="bulleted">Detailed Kitchen Cleaning and</li>
        <li class="bulleted">Vat Boil Outs</li>
        <li>Gurney High Pressure and</li>
        <li class="bulleted">Playground Cleaning</li>
        <li>General Facility Maintenance</li>
      </ul>
    </div>
    <div class="card card-upgrades">
      <svg class="card-icon" viewBox="0 0 110 120" fill="none" stroke="#cd5227" stroke-width="5" stroke-linejoin="round" stroke-linecap="round">
        <path d="M88 38a42 42 0 0 0-66-4"/>
        <path d="M22 82a42 42 0 0 0 66 4"/>
        <path d="M80 26l9 12-14 3"/>
        <path d="M30 94l-9-12 14-3"/>
        <path d="M55 36l-22 22h12v22h20V58h12z"/>
        <path d="M45 88h20"/>
      </svg>
      <h2><span class="accent">Business Upgrades</span><span class="dark">completed</span></h2>
      <p class="upgrade-text">We have upgraded and digitalised our reporting system for transparency across our services.</p>
      <p class="upgrade-text">Our Team Members have received ongoing refresher training to keep skills refreshed and Market aligned.</p>
    </div>
  </div>

  <svg class="service-panel" viewBox="0 0 1200 144" preserveAspectRatio="none">
    <path d="M445 144 L545 30 Q568 4 600 4 L1200 4 L1200 144 Z" fill="#ffffff"/>
  </svg>
  <div class="contact">
    <h3>Customer Service:</h3>
    <p>Welcome to call on Customer Service Ph@ 1300 555 019</p>
    <p>or Email: Service@brightvale.com.au for Service.</p>
  </div>
</div>
</body>
</html>
```